Venture Capital Firm Needs Website Redesign

We need a bold revamp of our website (https://halvenmoor.vc/)
which at the moment looks washed out. We want a crisp, fresh and unique look. Feel free to keep as much or as little content in the site. The only thing we need to keep is a team section. The site should convey a clear distinction between our 3 product lines: Venture Capital, Private Credit, and Crypto. Two versions of our logo are attached and they should not change. For design inspirations, we like http://www.plumridgecap.com/ for a more simple site and for a more built out site we like http://tallowgate.com/

Updates
Industry/Entity Type
Investment
Coding
Coded - Design and coding required
Number of Pages Required
1 page
Font styles to use
Colors
Designer to choose colors to be used in the design.
Requirements
Must have
- - Clear distinction between our 3 product lines: Venture Capital, Private Credit
- - Team section

Nice to have
- Some really creative aspect like http://www.plumridgecap.com/ has with the distinction between first, second, and third kind

```html
<!DOCTYPE html>
<html lang="en">
<head>
<meta charset="utf-8">
<title>Halvenmoor — Bridge technology and finance</title>
<link href="https://fonts.googleapis.com/css2?family=Poppins:wght@300;400;500;600;700&display=swap" rel="stylesheet">
<style>
:root{
  --green:#94a82e;
  --ink:#111214;
  --text:#55575c;
  --white:#ffffff;
  --grey-dark:#45464a;
  --grey-mid:#6b6c71;
  --grey-light:#eeeff0;
  --grey-line:#8a8b8f;
  --numeral-light:#eeeeef;
  --numeral-dark:rgba(255,255,255,.07);
}
*{margin:0;padding:0;box-sizing:border-box}
html,body{width:1200px;height:3346px;overflow:hidden}
body{position:relative;font-family:"Poppins",sans-serif;color:var(--text);background:var(--white)}
a{color:inherit;text-decoration:none}

/* header */
.site-header{position:absolute;left:0;top:0;width:1200px;height:62px;background:var(--white);z-index:5}
.brand{position:absolute;left:86px;top:16px;font-family:"Poppins",sans-serif;font-weight:400;font-size:28px;letter-spacing:1px;color:var(--ink)}
.main-nav{position:absolute;right:90px;top:24px;display:flex;gap:30px;font-size:12px;font-weight:600;letter-spacing:.6px;color:var(--ink)}
.menu-icon{position:absolute;right:60px;top:26px;width:16px}
.menu-icon span{display:block;height:2px;background:var(--ink);margin-bottom:3px}

/* shared */
.section-label{position:absolute;font-size:13px;font-weight:600;color:var(--ink)}
.section-label::before{content:"";position:absolute;left:0;top:-9px;width:150px;height:2px;background:var(--ink)}
.section-label.on-dark{color:var(--white)}
.section-label.on-dark::before{background:var(--ink)}
.section-label .accent{color:var(--green)}
.h-big{position:absolute;font-weight:700;font-size:46px;line-height:56px;color:var(--ink);letter-spacing:-.3px}
.body-copy{position:absolute;font-size:13px;line-height:21px;font-weight:300;color:var(--text)}
.btn-dark{position:absolute;width:184px;height:47px;background:var(--ink);color:var(--white);font-size:10px;font-weight:500;letter-spacing:1.2px;display:flex;align-items:center;padding:0 18px;justify-content:space-between}
.arrow{width:24px;height:10px}
.numeral{position:absolute;font-weight:700;line-height:1;z-index:0}

/* hero */
.hero{position:absolute;left:0;top:62px;width:1200px;height:585px;
  background:linear-gradient(180deg,#d9dcdf 0%,#e4e6e8 45%,#d3d5d7 100%)}
.hero-photo{position:absolute;inset:0}
.hero h1{top:205px;left:147px}
.hero .body-copy{top:325px;left:147px;width:290px;color:#333}
.slider-dots{position:absolute;left:570px;top:544px;display:flex;gap:7px}
.slider-dots i{width:8px;height:8px;border-radius:50%;background:rgba(255,255,255,.6)}
.slider-dots i:first-child{background:#fff}
.hero-mark{position:absolute;left:150px;top:480px;width:190px;height:190px;border:3px solid var(--ink);border-radius:50%;display:flex;align-items:center;justify-content:center;z-index:3;background:transparent}
.hero-mark span{font-size:22px;font-weight:500;color:var(--green)}

/* about */
.about{position:absolute;left:0;top:647px;width:1200px;height:524px;background:linear-gradient(180deg,#56575b 0%,#48494d 55%,#3f4044 100%);overflow:hidden}
.about-art{position:absolute;left:180px;top:240px;width:460px;height:284px;background:radial-gradient(ellipse at 45% 60%,rgba(120,121,125,.55),rgba(72,73,77,0) 70%)}
.about h2{left:147px;top:220px;color:var(--white)}
.about .body-copy{left:613px;top:227px;width:400px;color:#e8e8ea}
.about .btn-dark{left:613px;top:316px}

/* cards */
.card{position:absolute;top:1242px;width:290px;height:241px;background:var(--white);box-shadow:0 2px 10px rgba(0,0,0,.12)}
.card-team{left:147px}
.card-team .photo{height:158px;background:linear-gradient(135deg,#a7bd3b,#6f8a23);position:relative}
.card-team .photo-caption{position:absolute;left:18px;top:18px;color:#fff;font-weight:600;font-size:13px}
.card-team .photo-tag{position:absolute;left:30px;top:100px;color:#fff;font-weight:600;font-size:13px;line-height:17px}
.card-foot{position:absolute;left:0;right:0;bottom:0;height:83px;display:flex;align-items:center;justify-content:space-between;padding:0 28px 0 18px;font-size:10px;font-weight:600;letter-spacing:1.3px;color:var(--ink)}
.card-quote{left:455px;background:#7a7b7f}
.card-quote .quote-top{height:158px;text-align:center;color:#fff;padding-top:42px}
.card-quote .quote-top p{font-size:13px;font-weight:600;line-height:17px}
.card-quote .quote-top strong{display:block;font-size:20px;font-weight:600;margin-top:12px}
.card-quote .card-foot{background:var(--ink);color:#fff}
.card-quote .notch{position:absolute;left:140px;top:152px;width:0;height:0;border-left:6px solid transparent;border-right:6px solid transparent;border-bottom:6px solid var(--ink)}
.card-blog{left:763px}
.card-blog .photo{height:158px;background:linear-gradient(180deg,#1f5a8a 0%,#2d7db0 45%,#1b4f7c 46%,#0e2f4f 100%)}
.card-blog h3{position:absolute;left:18px;top:168px;font-size:16px;font-weight:600;color:var(--ink)}
.avatar{position:absolute;left:18px;top:197px;width:30px;height:30px;border-radius:50%;background:#8a8b8f}
.byline{position:absolute;left:56px;top:199px;font-size:10px;line-height:13px;color:#777}
.byline b{color:var(--green);font-weight:500}
.pager{position:absolute;right:16px;top:209px;font-size:12px;color:#999}

.divider{position:absolute;left:147px;top:1552px;width:906px;height:1px;background:#555}

/* venture */
.venture-squares{position:absolute;left:359px;top:1628px;display:flex;gap:2px}
.venture-squares i{width:24px;height:24px;display:block}
.tag-circle{position:absolute;border:3px solid var(--ink);border-radius:50%;display:flex;flex-direction:column;align-items:center;justify-content:center;z-index:2}
.tag-circle small{font-size:17px;font-weight:600;color:var(--green)}
.tag-circle strong{font-size:40px;font-weight:600;color:var(--ink);line-height:1}
.partner-row{position:absolute;display:flex;align-items:center;gap:46px}
.partner{font-size:15px;font-weight:500;color:#3c4b6a;display:flex;align-items:center;gap:6px}
.partner i{width:12px;height:12px;display:block;background:currentColor}

/* private credit */
.credit{position:absolute;left:0;top:2003px;width:1200px;height:526px;background:var(--grey-mid);overflow:hidden}
.credit .tag-circle{border-color:#fff}
.credit .tag-circle strong{color:#fff}

/* crypto */
.chart{position:absolute;left:660px;top:2598px;width:440px;height:380px;z-index:1}

/* footer */
.site-footer{position:absolute;left:0;top:3042px;width:1200px;height:304px;background:var(--grey-mid);color:#fff}
.footer-mark{position:absolute;left:90px;top:70px;width:186px;height:186px;border:3px solid #fff;border-radius:50%;display:flex;align-items:center;justify-content:center;font-size:20px;font-weight:500}
.footer-contact{position:absolute;left:607px;top:70px;font-size:13px;font-weight:600;line-height:20px}
.footer-links{position:absolute;left:832px;top:66px;font-size:13px;font-weight:600;line-height:23.5px;list-style:none}
.social{position:absolute;left:988px;top:68px;display:grid;grid-template-columns:28px 28px 28px;gap:18px 19px}
.social i{width:28px;height:28px;display:block}
.to-top{position:absolute;left:1093px;top:3009px;width:45px;height:42px;background:var(--ink);z-index:6;display:flex;align-items:center;justify-content:center}
</style>
</head>
<body>

<header class="site-header">
  <div class="brand">HALVENMOOR</div>
  <nav class="main-nav">
    <a href="#venture">VENTURE</a><a href="#credit">PRIVATE CREDIT</a><a href="#crypto">CRYPTO</a><a href="#about">ABOUT US</a><a href="#team">TEAM</a><a href="#blog">BLOG</a>
  </nav>
  <div class="menu-icon"><span></span><span></span><span></span></div>
</header>

<section class="hero">
  <div class="hero-photo" role="img" aria-label="Photograph of a steel arch bridge under a pale overcast sky"></div>
  <div class="section-label" style="left:147px;top:158px;padding-left:66px"><span class="accent">Halvenmoor</span></div>
  <h1 class="h-big">Bridge technology<br>and finance.</h1>
  <p class="body-copy">Halvenmoor operates at the intersection of technology and novel asset classes.</p>
  <div class="slider-dots"><i></i><i></i><i></i></div>
</section>
<div class="hero-mark"><span>Halvenmoor</span></div>

<section class="about" id="about">
  <div class="numeral" style="left:810px;top:120px;font-size:400px;color:rgba(0,0,0,.12)">3</div>
  <div class="about-art" role="img" aria-label="Grey folded paper sculpture in soft shadow"></div>
  <div class="section-label on-dark" style="left:147px;top:185px;padding-left:78px">About Us</div>
  <h2 class="h-big">We operates<br>three businesses.</h2>
  <p class="body-copy">Halvenmoor operates three businesses that bridge technology and finance. We invest in pre-seed venture capital, and build software for the companies we invest in.</p>
  <a class="btn-dark" href="#venture">VIEW DETAILS
    <svg class="arrow" viewBox="0 0 24 10"><path d="M0 5h22M17 1l5 4-5 4" fill="none" stroke="#fff" stroke-width="1.3"/></svg></a>
</section>

<article class="card card-team" id="team">
  <div class="photo" role="img" aria-label="Green-toned photograph of the team's office">
    <div class="photo-caption">Halvenmoor team</div>
    <div class="photo-tag">The very best helping<br>the very best.</div>
  </div>
  <div class="card-foot">MEET ALL
    <svg class="arrow" viewBox="0 0 24 10"><path d="M0 5h22M17 1l5 4-5 4" fill="none" stroke="#111" stroke-width="1.3"/></svg></div>
</article>

<article class="card card-quote">
  <div class="quote-top"><p>We would love to<br>hear from you.</p><strong>info@halvenmoor.vc</strong></div>
  <span class="notch"></span>
  <div class="card-foot">GET A QUOTE
    <svg class="arrow" viewBox="0 0 24 10"><path d="M0 5h22M17 1l5 4-5 4" fill="none" stroke="#fff" stroke-width="1.3"/></svg></div>
</article>

<article class="card card-blog" id="blog">
  <div class="photo" role="img" aria-label="Photograph of an iceberg in deep blue water"></div>
  <h3>How to build a “WOW”...</h3>
  <div class="avatar" role="img" aria-label="Author portrait"></div>
  <div class="byline">by <b>Oren Valdez</b><br>2 April 2018</div>
  <div class="pager">‹ &nbsp;<span style="color:#111">›</span></div>
</article>

<div class="divider"></div>

<section id="venture">
  <div class="numeral" style="left:915px;top:1625px;font-size:430px;color:var(--numeral-light)">1</div>
  <div class="section-label" style="left:147px;top:1636px;padding-left:84px">First<span style="color:var(--ink)">One</span></div>
  <div class="venture-squares"><i style="background:var(--green)"></i><i style="background:#2a2b2e"></i></div>
  <h2 class="h-big" style="left:147px;top:1672px">Venture Capital.</h2>
  <p class="body-copy" style="left:147px;top:1738px;width:485px">We invest in early-stage startups led by founders who are passionate and knowledgeable about the markets they serve. We have our own software developers and product managers. We work with the founders in our portfolio to help them bring products to market, earning equity for this work and for the cash we invest in their companies.</p>
  <div class="tag-circle" style="left:767px;top:1648px;width:206px;height:206px"><small>Invest In</small><strong>early</strong></div>
  <div class="partner-row" style="left:147px;top:1900px">
    <span class="partner" style="font-size:11px"><i></i>RIDGEWAY CAPITAL GROUP</span>
    <span class="partner" style="color:#7b5a8a"><i></i>Tovella</span>
    <span class="partner" style="color:#2a9fd8;font-size:22px;font-weight:400">Tinytrek</span>
    <span class="partner" style="color:#1d3c6e">Loomfield</span>
  </div>
</section>

<section class="credit" id="credit">
  <div class="numeral" style="left:80px;top:145px;font-size:380px;color:var(--numeral-dark)">2</div>
  <div class="tag-circle" style="left:307px;top:182px;width:182px;height:182px"><small>Provides</small><strong style="font-size:34px">capital</strong></div>
  <div class="section-label on-dark" style="left:613px;top:149px;padding-left:60px">Second<span style="color:var(--ink)">One</span></div>
  <h2 class="h-big" style="left:613px;top:186px;color:#fff">Private Credit.</h2>
  <p class="body-copy" style="left:613px;top:252px;width:450px;color:#eee">Halvenmoor Private Credit provides capital to lending businesses that are focused on using technology to establish new credit markets, create new credit products or dramatically re-invent an existing form of credit.</p>
  <div class="partner-row" style="left:613px;top:374px;gap:40px">
    <span class="partner" style="color:#fff;font-weight:600;font-size:15px"><i></i>Carrow Financial</span>
    <span class="partner" style="color:#fff"><i style="border-radius:50%"></i>Sprigline</span>
    <span class="partner" style="color:#fff;font-weight:400;letter-spacing:1px">BRIGHTLEDGER</span>
  </div>
</section>

<section id="crypto">
  <div class="numeral" style="left:790px;top:2560px;font-size:440px;color:var(--numeral-light)">3</div>
  <div class="section-label" style="left:147px;top:2631px;padding-left:78px">Third<span style="color:var(--ink)">One</span></div>
  <h2 class="h-big" style="left:147px;top:2676px">CRYPTO.</h2>
  <p class="body-copy" style="left:147px;top:2744px;width:440px">The Halvenmoor Crypto Index tracks the top 15 cryptocurrencies weighted by market cap and rebalanced twice a month. We believe this is the simplest and most cost effective way to obtain cryptocurrency exposure.</p>
  <a class="btn-dark" style="left:147px;top:2853px" href="#crypto">VIEW DETAILS
    <svg class="arrow" viewBox="0 0 24 10"><path d="M0 5h22M17 1l5 4-5 4" fill="none" stroke="#fff" stroke-width="1.3"/></svg></a>

  <svg class="chart" viewBox="0 0 440 380" font-family="Poppins, sans-serif">
    <text x="160" y="12" font-size="9" font-weight="600" fill="#333">HCI™ Cumulative Growth</text>
    <circle cx="110" cy="28" r="6" fill="var(--green)"/><text x="120" y="31" font-size="8" fill="#888">HCI™ (2236.86%)</text>
    <circle cx="210" cy="28" r="6" fill="#111"/><text x="220" y="31" font-size="8" fill="#888">Corvale Coin (777.41%)</text>
    <g stroke="#e2e3e5" stroke-width="1">
      <line x1="50" y1="280" x2="410" y2="280"/><line x1="50" y1="238" x2="410" y2="238"/>
      <line x1="50" y1="197" x2="410" y2="197"/><line x1="50" y1="155" x2="410" y2="155"/>
      <line x1="50" y1="113" x2="410" y2="113"/><line x1="50" y1="72" x2="410" y2="72"/>
      <line x1="50" y1="30" x2="410" y2="30"/>
    </g>
    <g font-size="8" fill="#777" text-anchor="end">
      <text x="38" y="283">0</text><text x="38" y="241">500</text><text x="38" y="200">1000</text>
      <text x="38" y="158">1500</text><text x="38" y="116">2000</text><text x="38" y="75">2500</text><text x="38" y="33">3000</text>
    </g>
    <g font-size="8" fill="#777" text-anchor="middle">
      <text x="50" y="295">Jan</text><text x="76" y="295">Feb</text><text x="102" y="295">Mar</text><text x="128" y="295">Apr</text>
      <text x="154" y="295">May</text><text x="180" y="295">Jun</text><text x="206" y="295">Jul</text><text x="232" y="295">Aug</text>
      <text x="258" y="295">Sep</text><text x="284" y="295">Oct</text><text x="310" y="295">Nov</text><text x="336" y="295">Dec</text>
      <text x="362" y="295">Jan</text><text x="385" y="295">Feb</text><text x="405" y="295">Mar</text>
    </g>
    <polyline fill="none" stroke="var(--green)" stroke-width="2.5" points="50,280 64,279.6 78,279.2 92,278.8 106,277.5 120,275 134,271.7 148,267.5 162,259.2 176,263.3 190,250.8 204,238.3 218,242.5 232,225.8 246,213.3 260,221.7 274,188.3 288,171.7 302,130 316,80 330,38.3 344,71.7 358,113.3 372,130 386,155 400,180"/>
    <polyline fill="none" stroke="#111" stroke-width="2.5" points="50,280 64,279.8 78,279.6 92,279.3 106,278.8 120,277.5 134,275.8 148,273.3 162,267.5 176,270 190,263.3 204,255 218,259.2 232,250.8 246,242.5 260,246.7 274,230 288,221.7 302,196.7 316,163.3 330,130 344,155 358,171.7 372,188.3 386,205 400,217.5"/>
    <g font-size="6" fill="#777" text-anchor="middle">
      <text x="225" y="312">Growth shown from index launch through the latest rebalance. Past results do not</text>
      <text x="225" y="321">predict future returns and figures are for illustration only.</text>
    </g>
  </svg>
</section>

<a class="to-top" href="#" aria-label="Back to top">
  <svg width="18" height="12" viewBox="0 0 18 12"><path d="M1 11l8-9 8 9" fill="none" stroke="#fff" stroke-width="2"/></svg>
</a>

<footer class="site-footer">
  <div class="footer-mark">Halvenmoor</div>
  <div class="footer-contact">info@halvenmoor.vc<br><br>318 Larkspur Avenue, Suite 604<br>Harlow Bay, NY<br>10092</div>
  <ul class="footer-links"><li>Venture</li><li>Private Credit</li><li>Crypto</li><li>About Us</li><li>Team</li><li>Blog</li></ul>
  <div class="social" aria-label="Social links">
    <i style="background:#3b5a98"></i><i style="background:#2aa3de"></i><i style="background:#d8473a"></i>
    <i style="background:#2cb3df"></i><i style="background:#c62b2b"></i>
  </div>
</footer>

</body>
</html>
```